Door Hanger for 20% off on dry cleaning

I need a door hanger (3.5" x 8.5" with a hole for the door handle) for a 20% off sale on dry cleaning. The business is called "Suds by Maplecrest" and is a full-service laundry. The store is a laundromat that is used by self-serve customers. We also do wash-and-fold laundry and dry cleaning.

Some requirements:
* Include the logo
* Includes the address of the business:
615 South 300 West
Provo, Utah
(behind Harbor Crust Pies)
* Include some indication of our other services (wash-and-fold laundry, coin laundry, comforters cleaned)
* Offer needs to include an expiration date (say, September 30, 2014).

The door hanger should be full-color with designs for both sides.
Updates

The sale is for 20% off of Dry Cleaning - not the other services. And I'd like both sides of the hanger to mention the sale - in case it gets hung backwards on the door.

Industry/Entity Type

Dry Cleaning

```html
<!DOCTYPE html>
<html lang="en">
<head>
<meta charset="utf-8">
<title>Suds by Maplecrest – Door Hanger</title>
<link href="https://fonts.googleapis.com/css2?family=Archivo+Black&family=Arimo:wght@400;700&display=swap" rel="stylesheet">
<style>
  :root {
    --sky: #a9d9f2;
    --royal: #1f57d9;
    --royal-deep: #123fae;
    --orange: #f2541f;
    --white: #ffffff;
    --ink-blue: #1a4fc9;
  }
  html, body { margin: 0; padding: 0; overflow: hidden; }
  body { width: 1200px; height: 2913px; background: var(--sky); }
  .hanger {
    position: relative; width: 1200px; height: 2913px; overflow: hidden;
    background: var(--sky); font-family: "Arimo", Arial, sans-serif; color: var(--white);
  }
  .hanger div, .hanger section { position: absolute; white-space: nowrap; line-height: 1; }
  .hole-art { position: absolute; left: 0; top: 0; }

  .panel {
    left: 0; top: 920px; width: 1200px; height: 1993px;
    background: var(--royal); border-top-right-radius: 130px;
  }
  .panel-edge {
    left: 1172px; top: 1194px; width: 14px; height: 1719px; background: var(--royal-deep);
  }
  .machine-art {
    left: 15px; top: 859px; width: 349px; height: 350px;
    background: linear-gradient(160deg, #7aa6f2, #1f57d9); border-radius: 16px;
  }
  .brand {
    left: 364px; top: 945px; width: 757px; height: 220px;
    background: var(--sky); border-top-right-radius: 60px;
    display: flex; align-items: center; justify-content: center;
  }
  .brand-name { font-weight: 700; font-size: 64px; color: var(--ink-blue); }

  .line-full { left: 96px; top: 1331px; font-weight: 700; font-size: 140px; letter-spacing: -3px; }
  .asterisk-top { left: 1080px; top: 1300px; font-weight: 700; font-size: 110px; }
  .amp { left: 110px; top: 1423px; font-weight: 700; font-size: 300px; }
  .line-self { left: 285px; top: 1457px; font-weight: 700; font-size: 128px; letter-spacing: -1px; }
  .line-mat { left: 285px; top: 1580px; font-weight: 400; font-size: 114px; }

  .coupon {
    left: 79px; top: 1757px; width: 1048px; height: 471px; box-sizing: border-box;
    background: var(--orange); border: 10px dashed var(--white); border-radius: 40px;
  }
  .coupon .deal {
    left: 30px; top: 60px; font-family: "Archivo Black", "Arial Black", sans-serif;
    font-size: 200px; letter-spacing: -4px; text-shadow: 8px 8px 0 var(--royal-deep);
  }
  .coupon .bang {
    left: 905px; top: -10px; font-family: "Archivo Black", "Arial Black", sans-serif;
    font-size: 380px; text-shadow: 10px 10px 0 var(--royal-deep);
  }
  .coupon .item {
    left: 30px; top: 250px; font-family: "Archivo Black", "Arial Black", sans-serif;
    font-size: 76px; letter-spacing: 2px; text-shadow: 5px 5px 0 var(--royal-deep);
  }
  .coupon .expires {
    left: 0; width: 1028px; top: 372px; text-align: center; font-weight: 700; font-size: 38px;
  }

  .services { top: 2300px; font-weight: 700; }
  .services h3 { margin: 0; font-size: 50px; line-height: 1; }
  .services h3 span { font-size: 66px; vertical-align: -12px; }
  .services ul { margin: 10px 0 0 50px; padding: 0; list-style: none; font-size: 30px; line-height: 1.15; }
  .services li::before { content: "•"; margin-right: 4px; }
  .services.full { left: 128px; }
  .services.self-list { left: 718px; }

  .locate {
    left: 79px; top: 2549px; width: 1042px; height: 262px;
    background: var(--sky); border-radius: 40px;
  }
  .locate h2 {
    position: absolute; left: 0; width: 1042px; top: 12px; margin: 0; text-align: center;
    font-size: 100px; font-weight: 700; color: var(--orange); line-height: 1;
  }
  .locate .address {
    left: 0; width: 1042px; top: 138px; text-align: center;
    font-weight: 700; font-size: 56px; letter-spacing: -1px; color: var(--ink-blue);
  }
  .locate .landmark {
    left: 0; width: 1042px; top: 203px; text-align: center; font-size: 48px; color: var(--ink-blue);
  }
</style>
</head>
<body>
<main class="hanger">
  <svg class="hole-art" width="1200" height="932" viewBox="0 0 1200 932" aria-hidden="true">
    <line x1="0" y1="660" x2="340" y2="520" stroke="#000" stroke-width="4"/>
    <circle cx="603" cy="481" r="291" fill="#fff" stroke="#000" stroke-width="4"/>
  </svg>

  <div class="panel"></div>
  <div class="panel-edge"></div>

  <div class="machine-art" role="img" aria-label="Illustration of a blue front-loading washing machine"></div>

  <div class="brand"><span class="brand-name">Suds by Maplecrest</span></div>

  <div class="line-full">FULL-SERVICE</div>
  <div class="asterisk-top">*</div>
  <div class="amp">&amp;</div>
  <div class="line-self">SELF-SERVE</div>
  <div class="line-mat">LAUNDROMAT</div>

  <section class="coupon">
    <div class="deal">20% off</div>
    <div class="bang">!</div>
    <div class="item">ON DRY CLEANING</div>
    <div class="expires">OFFER EXPIRES: SEPTEMBER 30, 2014.</div>
  </section>

  <section class="services full">
    <h3><span>*</span>FULL-SERVICE:</h3>
    <ul><li>WASH-AND-FOLD LAUNDRY</li><li>DRY CLEANING</li><li>COMFORTERS</li></ul>
  </section>
  <section class="services self-list">
    <h3><span>*</span>SELF-SERVE:</h3>
    <ul><li>COIN LAUNDRY</li></ul>
  </section>

  <section class="locate">
    <h2>WHERE ARE WE?</h2>
    <div class="address">615 SOUTH 300 WEST, PROVO, UTAH</div>
    <div class="landmark">(BEHIND HARBOR CRUST PIES)</div>
  </section>
</main>
</body>
</html>
```